CREATE A BUSINESS CARD FOR A BOAT CLEANING SERVICE

WE ARE STARTING A NEW BOAT CLEANING BUSINESS. WE DIVE UNDERWATER TO CLEAN BOAT HULLS, JETTIES, UNDERWATER STRUCTURES ETC. WE ARE LOOKING FOR AN UPPERMARKET MODERN LOGO AND BUSINESS CARD AS ALOT OF OUR TARGET MARKET WILL BE HIGH END. YOU HAVE TO DESIGN A BUSINESS CARD AND LOGO SEPERATELY .
THE BUSINESS CARD DIMESNION MUST BE STANDARD SIZE.
The standard dimensions of a printed business card are 3.5 x 2 inches

Target Market(s)

UNDERWATER SERVICED

Industry/Entity Type

Business

Contact Information for Business Card

HALDANE SUBSEA SERVICES

Font styles to use
Serif

Colors

Designer to choose colors to be used in the design.

Requirements
Must have
• HALDANE
Nice to have
• dark
Should not have
• more than 3 colors

```html
<!DOCTYPE html>
<html lang="en">
<head>
<meta charset="UTF-8">
<title>Haldane Subsea Services – Business Card</title>
<link rel="stylesheet" href="https://fonts.googleapis.com/css2?family=Cinzel:wght@500&family=Jost:wght@500;600&display=swap">
<style>
  :root {
    --backdrop: #dedde3;
    --card-black: #020305;
    --deep-blue: #0a3f8a;
    --bright-blue: #1f6fd6;
    --gold: #a59a73;
    --white: #f4f4f4;
  }
  * { margin: 0; padding: 0; box-sizing: border-box; }
  html, body {
    width: 1200px;
    height: 1200px;
    overflow: hidden;
    background: var(--backdrop);
  }
  .card {
    position: absolute;
    left: 100px;
    top: 314px;
    width: 1000px;
    height: 572px;
    background: var(--card-black);
    overflow: hidden;
    box-shadow: 0 14px 40px rgba(0, 0, 0, 0.18);
  }
  .card__photo {
    position: absolute;
    right: 0;
    top: 0;
    width: 620px;
    height: 420px;
    background:
      radial-gradient(ellipse 55% 60% at 62% 55%, var(--bright-blue) 0%, var(--deep-blue) 35%, rgba(4, 20, 50, 0.6) 65%, rgba(2, 3, 5, 0) 100%);
  }
  .brand {
    position: absolute;
    left: 120px;
    top: 150px;
  }
  .brand__row {
    display: flex;
    align-items: center;
    gap: 18px;
  }
  .brand__dot {
    width: 14px;
    height: 14px;
    background: var(--gold);
  }
  .brand__name {
    font-family: "Cinzel", serif;
    font-weight: 500;
    font-size: 64px;
    letter-spacing: 0.12em;
    color: var(--gold);
    line-height: 1;
  }
  .brand__tagline {
    margin-top: 10px;
    margin-left: 34px;
    font-family: "Jost", sans-serif;
    font-weight: 500;
    font-size: 15px;
    letter-spacing: 0.62em;
    color: var(--white);
  }
  .details {
    position: absolute;
    left: 120px;
    top: 418px;
    font-family: "Jost", sans-serif;
  }
  .details__service {
    font-weight: 600;
    font-size: 17px;
    letter-spacing: 0.16em;
    color: var(--gold);
    text-transform: uppercase;
  }
  .details__contact {
    margin-top: 10px;
    font-weight: 600;
    font-size: 19px;
    letter-spacing: 0.08em;
    color: var(--white);
    display: flex;
    gap: 20px;
  }
  .details__sep { color: var(--white); }
</style>
</head>
<body>
  <div class="card">
    <div class="card__photo" role="img" aria-label="Photo of a scuba diver silhouetted beneath a boat hull in deep blue water"></div>

    <div class="brand">
      <div class="brand__row">
        <span class="brand__dot"></span>
        <span class="brand__name">HALDANE</span>
      </div>
      <div class="brand__tagline">SUBSEA SERVICES</div>
    </div>

    <div class="details">
      <div class="details__service">Underwater hull &amp; structure cleaning</div>
      <div class="details__contact">
        <span>04 218 560 337</span>
        <span class="details__sep">|</span>
        <span>hello@haldanesubsea.com</span>
        <span class="details__sep">|</span>
        <span>www.haldanesubseaservices.com</span>
      </div>
    </div>
  </div>
</body>
</html>
```